Web Design Project

Please design a new website template for Calderbrook as follows -

Existing Website - http://www.calderbrook.com.au/

Logo - http://rankyoursitenow.com/Design/calderbrook-logo

Navigation - Top Horizontal

Colours: Pink and purple from attached logo (do not use the bright pink from the existing website)

Page Structure: Home, About Us, Services, The Team, Key Contacts, Our Values, Send Resume, Timesheets, Candidates, Clients, Location, Contact Us.

The template should include an enquiry from on all pages with fields: Name, Phone, Email, Enquiry

The template should include their phone number in the top right corner - (08) 9271 5608

It should include a tag line: Temporary & Permanent Support Staff Specialists

The Footer:
Level 5, 7 Pemberly Terrace
SUBIACO
WA 6008
Phone - (08) 9271 5608
Fax - (08) 9271 5690
Email - admin@calderbrook.com.au

Websites they like - http://www.markdunwoodycosmeticclinic.com.au/ (preferably keep the text on a white background on this site)

Include a button/icon for - Job Listings

Home page text - Use what is on their existing website (you can reduce the number of bullet points)

```html
<!DOCTYPE html>
<html lang="en">
<head>
<meta charset="utf-8">
<title>Calderbrook - The Recruitment Bureau</title>
<link rel="stylesheet" href="https://fonts.googleapis.com/css2?family=Open+Sans:ital,wght@0,400;0,600;0,700;1,700&family=Cinzel:wght@400&family=Arimo:ital,wght@0,400;0,700;1,400&display=swap">
<style>
:root{
  --pink:#e5489c;
  --pink-deep:#d6307f;
  --purple:#4b2c87;
  --purple-card:#5a2f8c;
  --ink:#222;
  --grey-text:#333;
  --tab:#3b3b3b;
  --footer:#2a2a2a;
  --footer-bar:#1f1f1f;
  --light:#f4f4f4;
}
*{box-sizing:border-box;margin:0;padding:0}
html,body{width:1114px;height:1200px;overflow:hidden;background:#fff}
body{position:relative;font-family:"Arimo",Arial,sans-serif;color:var(--ink)}
.abs{position:absolute}

.site-header{left:0;top:0;width:1114px;height:137px;background:var(--pink)}
.brand{left:159px;top:30px;display:flex;align-items:center;gap:10px}
.brand-mark{width:18px;height:18px;border-radius:50%;background:#2a1a3a}
.brand-name{font-family:"Open Sans",sans-serif;font-weight:600;font-size:29px;letter-spacing:1px;color:#2a1a3a}
.brand-tag{left:200px;top:81px;font-family:"Open Sans",sans-serif;font-size:8px;letter-spacing:1px;color:#2a1a3a}
.header-phone{left:750px;top:34px;display:flex;align-items:center;gap:10px;font-family:"Cinzel",serif;font-size:22px;color:#fff}

.main-nav{left:161px;top:109px;display:flex;gap:5px}
.main-nav a{display:flex;align-items:center;justify-content:center;height:28px;border-radius:4px 4px 0 0;background:var(--tab);color:#fff;font-family:"Open Sans",sans-serif;font-size:10px;text-decoration:none}
.main-nav a.active{background:#ececec;color:#333}
.nav-rule{left:0;top:137px;width:1114px;height:5px;background:#d9d9d9}

.hero{left:156px;top:154px;width:796px;height:337px;background:#ececec;border:1px solid #d2d2d2}
.hero-photo{left:6px;top:5px;width:784px;height:326px;background:linear-gradient(100deg,#c9c4bd 0%,#8a7b6c 35%,#4b4a52 65%,#2c2c33 100%)}
.enquiry{left:704px;top:183px;width:224px;height:278px;border:2px solid #777;border-radius:10px;background:linear-gradient(#1b1b1b,#333)}
.enquiry h2{position:absolute;left:18px;top:8px;font-family:"Cinzel",serif;font-weight:400;font-size:22px;color:#fff}
.field{position:absolute;left:7px;font-size:12px;color:#fff;letter-spacing:.5px}
.input{position:absolute;left:62px;width:141px;height:22px;background:#fff;border:1px solid #999}
.callback{position:absolute;left:14px;top:227px;width:182px;height:31px;border-radius:6px;background:linear-gradient(var(--pink),var(--pink-deep));color:#fff;font-family:"Cinzel",serif;font-size:14px;display:flex;align-items:center;justify-content:center}

.intro-band{left:0;top:508px;width:1114px;height:120px;background:linear-gradient(#e6e6e6,#fff)}
.intro-photo{left:154px;top:514px;width:209px;height:210px;background:#d9d9d9;padding:5px}
.intro-photo div{width:100%;height:100%;background:linear-gradient(135deg,#b9ad9c,#3a3a42)}
.intro-title{left:377px;top:510px;font-family:"Open Sans",sans-serif;font-style:italic;font-weight:700;font-size:24px;color:#555}
.intro-title span{color:var(--purple)}
.intro-sub{left:377px;top:541px;font-family:"Open Sans",sans-serif;font-style:italic;font-weight:700;font-size:13px;color:#333}
.copy{font-style:italic;font-size:11px;line-height:17.2px;color:var(--grey-text);letter-spacing:.2px}
.copy-a{left:380px;top:563px;width:562px}
.copy-b{left:158px;top:730px;width:780px}
.divider{left:158px;top:776px;width:768px;height:1px;background:#ccc}

.roles{top:790px;list-style:none}
.roles li{font-weight:700;font-size:10.5px;line-height:19px;color:#333;letter-spacing:.3px}
.roles li::before{content:"»";color:var(--purple);margin-right:6px}
.profile{left:715px;top:784px;width:214px;height:120px;border:2px solid #bbb;border-radius:4px;background:linear-gradient(var(--purple-card),#3c1f6a)}
.profile-photo{position:absolute;left:0;top:4px;width:80px;height:112px;background:linear-gradient(#6b4a3e,#b12a2a)}
.profile h3{position:absolute;left:82px;top:12px;font-size:17px;line-height:20px;color:#fff;font-weight:700}
.profile p{position:absolute;left:84px;top:62px;width:125px;font-size:10px;line-height:13.5px;color:#fff}
.profile .more{position:absolute;right:8px;top:103px;font-size:10px;color:#fff}

.site-footer{left:0;top:923px;width:1114px;height:220px;background:var(--footer)}
.foot-h{font-family:"Open Sans",sans-serif;font-weight:700;font-size:23px;color:#fff;letter-spacing:.5px}
.quote{left:146px;top:972px;font-family:Georgia,serif;font-size:30px;color:#ddd;line-height:1}
.mission{left:170px;top:983px;width:240px;font-style:italic;font-size:10.5px;line-height:17px;color:#eee}
.map{left:455px;top:978px;width:205px;height:143px;background:linear-gradient(135deg,#e8e6df,#d9d6c8)}
.address{left:743px;top:978px;font-weight:700;font-size:12px;line-height:15.5px;color:var(--pink)}
.contact-lines{left:745px;top:1028px;font-size:10.5px;line-height:15.5px;color:#eee;letter-spacing:.4px}
.social{left:740px;top:1082px;display:flex;gap:8px;align-items:flex-end}
.badge{width:70px;height:42px;border-radius:20px;background:#3a9bd6}
.sq{width:24px;height:24px;border-radius:4px;background:#e6e6e6}
.foot-bar{left:0;top:1143px;width:1114px;height:57px;background:var(--footer-bar);border-top:1px solid #444}
.foot-nav{left:0;width:1114px;top:1153px;display:flex;justify-content:center;gap:32px;font-size:9.5px;color:#fff;letter-spacing:.3px}
.copyright{left:0;width:1114px;top:1176px;text-align:center;font-size:10px;color:#fff;letter-spacing:.3px}
</style>
</head>
<body>

<header class="site-header abs"></header>
<div class="brand abs"><span class="brand-mark"></span><span class="brand-name">CALDERBROOK</span></div>
<div class="brand-tag abs">THE RECRUITMENT BUREAU</div>
<div class="header-phone abs">
  <svg width="36" height="32" viewBox="0 0 36 32" aria-hidden="true">
    <path d="M3 10c0-5 6-8 15-8s15 3 15 8l-6 2-2-4H11l-2 4z" fill="#222"/>
    <rect x="7" y="13" width="22" height="16" rx="3" fill="#222"/>
    <circle cx="18" cy="21" r="5" fill="#eee"/>
  </svg>
  <span>08 9271 5608</span>
</div>

<nav class="main-nav abs">
  <a class="active" style="width:62px">About Us</a>
  <a style="width:61px">Services</a>
  <a style="width:67px">The Team</a>
  <a style="width:72px">Key Contacts</a>
  <a style="width:62px">Our Values</a>
  <a style="width:73px">Send Resume</a>
  <a style="width:74px">Timesheets</a>
  <a style="width:73px">Candidates</a>
  <a style="width:62px">Clients</a>
  <a style="width:64px">Location</a>
  <a style="width:68px">Contact Us</a>
</nav>
<div class="nav-rule abs"></div>

<section class="hero abs">
  <div class="hero-photo abs" role="img" aria-label="Photo of business people reviewing documents around a laptop"></div>
</section>
<form class="enquiry abs">
  <h2>Find Out More</h2>
  <span class="field" style="top:56px">Name:</span><span class="input" style="top:51px"></span>
  <span class="field" style="top:87px">Phone:</span><span class="input" style="top:82px"></span>
  <span class="field" style="top:118px">Email:</span><span class="input" style="top:113px"></span>
  <span class="field" style="top:149px">Enquiry:</span><span class="input" style="top:144px;height:74px"></span>
  <span class="callback">Request a Call Back</span>
</form>

<div class="intro-band abs"></div>
<div class="intro-photo abs"><div role="img" aria-label="Photo of two colleagues working on paperwork at a desk"></div></div>
<h1 class="intro-title abs"><span>Calderbrook</span> - The Recruitment Bureau</h1>
<p class="intro-sub abs">"Support Staff Specialists - Temporary and Permanent"</p>
<p class="copy copy-a abs">Calderbrook has impeccable credentials. Our experienced and thoroughly professional team services a broad range of blue-chip national and multi-national companies with the recruitment of temporary and permanent staff in the areas of:Calderbrook has impeccable credentials. Our experienced and thoroughly professional team services a broad range of blue-chip national and multi-national companies with the recruitment of temporary and permanent staff in the areas of:Calderbrook has impeccable credentials.<br><br>Our experienced and thoroughly professional team services a broad range with the recruitment of temporary and permanent staff in the areas of:Calderbrook has impeccable of blue-chip national and multi-national companies with the recruitment of temporary and permanent staff in the areas of:</p>
<p class="copy copy-b abs">Our experienced and thoroughly professional team services a broad range of blue-chip national and multi-national companies with the recruitment of temporary and permanent staff in the areas of:Calderbrook has impeccable credentials.</p>
<div class="divider abs"></div>

<ul class="roles abs" style="left:163px"><li>Administration</li><li>Personal Assistant</li><li>Executive Assistant</li><li>Reception</li><li>Legal</li></ul>
<ul class="roles abs" style="left:357px"><li>Secretaries</li><li>Accounts Clerk</li><li>Project Engineering</li><li>Construction and Property</li><li>Accounting</li></ul>
<ul class="roles abs" style="left:549px"><li>Customer Service</li><li>Data Entry</li><li>Cell Centre</li><li>Project Engineering</li></ul>

<aside class="profile abs">
  <div class="profile-photo" role="img" aria-label="Portrait of the company director"></div>
  <h3>Marissa<br>Calderbrook</h3>
  <p>Our experienced and thoroughly professional team services.</p>
  <span class="more">read more..</span>
</aside>

<footer class="site-footer abs"></footer>
<h2 class="foot-h abs" style="left:171px;top:938px">Our Mission</h2>
<h2 class="foot-h abs" style="left:458px;top:936px">Location</h2>
<h2 class="foot-h abs" style="left:742px;top:938px">Contact Us</h2>
<span class="quote abs">&ldquo;</span>
<p class="mission abs">To be the recruitment company of choice. To work together with our clients to provide services that are seen as creative and value-for-money. To be recognised and respected both within our own industry and that of our clients; and to consistently demonstrate our professionalism and passion for business.</p>
<div class="map abs" role="img" aria-label="Street map showing the office location in Subiaco"></div>
<p class="address abs">Level 5, 7 Pemberly Terrace<br>SUBIACO<br>WA 6008</p>
<p class="contact-lines abs">Phone - (08) 9271 5608<br>Fax - (08) 9271 5690<br>Email - admin@calderbrook.com.au</p>
<div class="social abs"><span class="badge"></span><span class="sq" style="margin-left:10px"></span><span class="sq"></span><span class="sq"></span></div>

<div class="foot-bar abs"></div>
<nav class="foot-nav abs"><span>HOME</span><span>ABOUT US</span><span>THE TEAM</span><span>RESUME TIPS</span><span>TIMESHEETS</span><span>SEND RESUME</span><span>CANDIDATES</span><span>LOCATION</span><span>CONTACT US</span></nav>
<p class="copyright abs">© 2012 Calderbrook - The Recruitment Bureau</p>

</body>
</html>
```